Corwin's Knuckle Balm - Premium Penetrating Lubricant

Text should read:
Corwin's Knuckle Balm Premium Penetrating Lubricant

Formulated to lubricate hard to reach areas.

Contains additives that boost lubricity, inhibit corrosion and clean.

Penetrates through rust, stops rust and frees up parts. Use as a mechanical repair assistant.

Available in 5 gallon containers. Ships via ground within Continental USA.

Distributed by Tressel Fabrique LLC 4817 Harlow Pike Ext. Roanoke Va. 24019

Resellers welcome

55 gallon drums available. Please contact customer support via email.

Description and features:
This website will require a shopping cart.

There will need to be a link to download the msds and an email link to customer support.

```html
<!DOCTYPE html>
<html lang="en">
<head>
<meta charset="utf-8">
<title>Corwin's Knuckle Balm – Premium Penetrating Lubricant</title>
<link rel="stylesheet" href="https://fonts.googleapis.com/css2?family=Open+Sans:wght@400;600;700;800&family=Lato:wght@400;700&display=swap">
<style>
:root{
  --brand-red:#c8102e;
  --ink:#333;
  --muted:#8a8a8a;
  --rule:#d5d5d5;
  --teal-dark:#0f6b86;
  --teal-light:#3aa6c2;
  --button:#1d6a83;
  --button-edge:#0e4a5e;
  --cart-bg:#34495e;
  --cart-side:#4b6d92;
  --cart-accent:#5fc6f2;
  --checkout-dark:#1c5a8c;
  --checkout-light:#2f82c2;
  --footer-bg:#2b2b2b;
  --footer-text:#d9d9d9;
  --link-blue:#3a9be0;
  --white:#fff;
}
*{box-sizing:border-box;margin:0;padding:0}
html,body{width:694px;height:1200px;overflow:hidden;background:var(--white)}
body{position:relative;font-family:"Open Sans",Arial,sans-serif;color:var(--ink)}
.abs{position:absolute}

/* header */
.login{top:8px;left:446px;display:flex;gap:3px}
.login-field{width:62px;height:11px;background:#e3e3e3;border:1px solid #c9c9c9;font-size:5.5px;color:#777;padding-left:4px;line-height:9px}
.login-btn{width:22px;height:11px;margin-left:6px;background:var(--brand-red);border-radius:2px;color:var(--white);font-size:5.5px;text-align:center;line-height:11px}
.brand{top:27px;left:87px;width:128px}
.brand-name{font-weight:800;font-size:15.5px;line-height:16px;color:var(--brand-red);text-transform:uppercase}
.brand-tag{margin-top:3px;font-weight:700;font-size:6px;color:var(--brand-red);text-align:center}
.social-top{top:43px;left:512px;display:flex;gap:4px}
.social-top span{width:16px;height:16px;border-radius:50%;background:#2e2e2e}
.social-top span.rss{background:var(--brand-red)}
.nav-rule{left:0;width:694px;height:1px;background:var(--rule)}
.nav{top:78px;left:0;width:694px;height:14px;font-size:9.5px;color:#666;letter-spacing:.2px}
.nav a{position:absolute;top:0;color:inherit;text-decoration:none}
.nav a.active{color:#111}
.nav a.active::after{content:"";position:absolute;left:0;right:0;top:12px;height:2px;background:var(--brand-red)}

/* hero */
.hero{top:95px;left:0;width:694px;height:233px;background:radial-gradient(ellipse at 65% 35%,var(--teal-light),var(--teal-dark) 80%)}
.slider{top:13px;left:87px;width:257px;height:201px;background:var(--white);border:1px solid #ccc}
.slide-photo{height:172px;background:linear-gradient(135deg,#8a2a22,#5a3a2e 45%,#9d8a73 70%,#3d3430)}
.slide-caption{height:29px;display:flex;align-items:center;justify-content:center;gap:8px;font-size:9.5px;color:#222}
.arrow-btn{width:19px;height:19px;border-radius:50%;border:1px solid #ccc;background:#f4f4f4;display:flex;align-items:center;justify-content:center}
.hero-copy{top:32px;left:352px;width:248px;color:var(--white);font-size:7.6px;font-weight:700;line-height:10px;text-align:center}
.hero-copy p{margin-bottom:9px}

/* products */
.product{width:132px;height:165px;background:#f5f5f5;box-shadow:0 1px 6px rgba(0,0,0,.25)}
.product-photo{position:absolute;top:0;left:12px;width:102px;height:102px;background:radial-gradient(ellipse at 50% 45%,#2b3550,#0c0f18 70%,#4a4030)}
.product-base{position:absolute;top:102px;left:0;right:0;bottom:0;border-top:1px solid #ddd}
.qty{position:absolute;top:9px;right:8px;display:flex;align-items:center;gap:4px}
.qty-label{font-size:5.5px;color:#aaa}
.qty-box{width:36px;height:19px;border:1px solid #bbb;border-radius:3px;background:var(--white);font-size:10px;padding-left:6px;line-height:17px;position:relative}
.qty-box svg{position:absolute;right:3px;top:3px}
.add-btn{position:absolute;left:8px;top:35px;width:116px;height:19px;background:var(--button);border:1px solid var(--button-edge);color:var(--white);font-size:7px;font-weight:700;display:flex;align-items:center;justify-content:center;gap:4px}

/* cart */
.cart{top:762px;left:195px;width:295px;height:130px;background:var(--cart-bg);box-shadow:0 2px 3px rgba(0,0,0,.3)}
.cart-title{position:absolute;left:25px;top:20px;font-size:22px;font-weight:700;color:var(--cart-accent)}
.cart-line{position:absolute;left:25px;top:52px;width:120px;height:2px;background:var(--cart-accent)}
.cart-total{position:absolute;left:25px;top:70px;font-size:17px;font-weight:700;color:var(--white)}
.cart-qty{position:absolute;left:25px;top:96px;font-size:12px;font-weight:700;color:var(--cart-accent)}
.cart-action{position:absolute;left:208px;width:87px;height:64px;background:var(--cart-side);color:var(--white);font-size:12.5px;text-align:center;padding-top:8px}
.cart-action svg{display:block;margin:0 auto 4px}

/* checkout */
.checkout{top:913px;left:0;width:694px;height:151px;background:linear-gradient(160deg,var(--checkout-light),var(--checkout-dark))}
.pay-card{position:absolute;left:184px;top:8px;width:273px;height:133px;background:#f2f2f2;border-radius:3px;box-shadow:0 1px 4px rgba(0,0,0,.35)}
.tabs{position:absolute;left:136px;top:4px;width:137px;height:14px;display:flex;font-size:4.5px;color:#444}
.tabs span{flex:1;text-align:center;line-height:14px;border-left:1px solid #ddd;background:#f8e8cf}
.tabs span+span{background:#e9e9e9}
.summary{position:absolute;left:14px;top:-4px;width:108px;height:137px;background:var(--white);box-shadow:0 0 4px rgba(0,0,0,.2);padding:5px 6px;font-size:4px;color:#999}
.summary-item{font-size:6.5px;color:#444;margin-top:2px;width:60px;line-height:8px}
.summary-price{position:absolute;right:6px;top:9px;font-size:9px;color:#777}
.lbl{position:absolute;font-size:3.5px;color:#999;text-transform:uppercase}
.fld{position:absolute;height:9px;border:1px solid #aaa;background:var(--white);font-size:4.5px;color:#222;padding-left:2px;line-height:7px;white-space:nowrap;overflow:hidden}
.order-btn{position:absolute;left:140px;top:115px;width:124px;height:13px;border-radius:2px;background:linear-gradient(#7f9fbf,#4d6f93);color:var(--white);font-size:5.5px;font-weight:700;text-align:center;line-height:13px}
.fine{position:absolute;font-size:3.8px;color:#dbe7f2}

/* footer */
.footer{top:1064px;left:0;width:694px;height:136px;background:var(--footer-bg);font-family:"Lato",Arial,sans-serif;color:var(--footer-text)}
.footer h3{position:absolute;top:15px;font-size:7.5px;font-weight:700;color:var(--white)}
.about-copy{position:absolute;left:121px;top:35px;width:165px;font-size:5.6px;line-height:9.2px}
.signoff{position:absolute;left:206px;top:101px;font-size:5.6px}
.signoff b{color:var(--white)}
.follow{position:absolute;left:337px;top:32px;font-size:6.3px}
.follow li{list-style:none;display:flex;align-items:center;gap:7px;height:21px}
.follow li span{width:13px;height:13px;border-radius:50%;background:var(--white)}
.follow li.hl{color:var(--link-blue)}
.follow li.hl span{background:var(--link-blue)}
.contact{position:absolute;left:494px;top:36px;font-size:6px;line-height:8px}
.contact .row{display:flex;gap:8px;margin-bottom:9px}
.contact a{color:var(--link-blue);text-decoration:none}
</style>
</head>
<body>

<header>
  <div class="abs login">
    <div class="login-field">Email adress</div>
    <div class="login-field">Password</div>
    <div class="login-btn">Login</div>
  </div>
  <div class="abs brand">
    <div class="brand-name">Corwin's Knuckle Balm</div>
    <div class="brand-tag">Premium Penetrating Lubricant</div>
  </div>
  <div class="abs social-top"><span></span><span></span><span></span><span></span><span class="rss"></span></div>
  <div class="abs nav-rule" style="top:70px"></div>
  <nav class="abs nav">
    <a class="active" href="#" style="left:183px">HOME</a>
    <a href="#" style="left:241px">PRODUCTS</a>
    <a href="#" style="left:322px">NEWS</a>
    <a href="#" style="left:381px">ABOUT US</a>
    <a href="#" style="left:457px">CONTACT US</a>
  </nav>
  <div class="abs nav-rule" style="top:93px"></div>
</header>

<section class="abs hero">
  <div class="abs slider">
    <div class="slide-photo" role="img" aria-label="Close-up photograph of greased gears and copper lubrication lines"></div>
    <div class="slide-caption">
      <span class="arrow-btn"><svg width="7" height="8" viewBox="0 0 7 8"><path d="M5 1 2 4l3 3" fill="none" stroke="#b11" stroke-width="1.6"/></svg></span>
      Lorem ipsum dolor sit amet
      <span class="arrow-btn"><svg width="7" height="8" viewBox="0 0 7 8"><path d="M2 1l3 3-3 3" fill="none" stroke="#b11" stroke-width="1.6"/></svg></span>
    </div>
  </div>
  <div class="abs hero-copy">
    <p>Contains additives that boost lubricity, inhibit corrosion and clean.</p>
    <p>Penetrates through rust, stops rust and frees up parts. Use as a mechanical repair assistant.</p>
    <p>Available in 5 gallon containers. Ships via ground within Continental USA.</p>
    <p>Distributed by Tressel Fabrique LLC 4817 Harlow Pike Ext. Roanoke Va. 24019</p>
    <p>Resellers are welcome!</p>
    <p>55 gallon drums available. Please contact customer support via email.</p>
  </div>
</section>

<main>
  <div class="abs product" style="left:114px;top:369px">
    <div class="product-photo" role="img" aria-label="Photo of a 5 gallon black pail of lubricant"></div>
    <div class="product-base">
      <div class="qty"><span class="qty-label">QTY:</span><div class="qty-box">1<svg width="6" height="11" viewBox="0 0 6 11"><path d="M0 4 3 1l3 3zM0 7l3 3 3-3z" fill="#444"/></svg></div></div>
      <div class="add-btn"><svg width="7" height="7" viewBox="0 0 7 7"><path d="M0 2h7L6 6H1z" fill="#fff"/></svg>ADD TO CART</div>
    </div>
  </div>
  <div class="abs product" style="left:279px;top:369px">
    <div class="product-photo" role="img" aria-label="Photo of a 5 gallon black pail of lubricant"></div>
    <div class="product-base">
      <div class="qty"><span class="qty-label">QTY:</span><div class="qty-box">1<svg width="6" height="11" viewBox="0 0 6 11"><path d="M0 4 3 1l3 3zM0 7l3 3 3-3z" fill="#444"/></svg></div></div>
      <div class="add-btn"><svg width="7" height="7" viewBox="0 0 7 7"><path d="M0 2h7L6 6H1z" fill="#fff"/></svg>ADD TO CART</div>
    </div>
  </div>
  <div class="abs product" style="left:449px;top:369px">
    <div class="product-photo" role="img" aria-label="Photo of a 5 gallon black pail of lubricant"></div>
    <div class="product-base">
      <div class="qty"><span class="qty-label">QTY:</span><div class="qty-box">1<svg width="6" height="11" viewBox="0 0 6 11"><path d="M0 4 3 1l3 3zM0 7l3 3 3-3z" fill="#444"/></svg></div></div>
      <div class="add-btn"><svg width="7" height="7" viewBox="0 0 7 7"><path d="M0 2h7L6 6H1z" fill="#fff"/></svg>ADD TO CART</div>
    </div>
  </div>
  <div class="abs product" style="left:114px;top:563px">
    <div class="product-photo" role="img" aria-label="Photo of a 5 gallon black pail of lubricant"></div>
    <div class="product-base">
      <div class="qty"><span class="qty-label">QTY:</span><div class="qty-box">1<svg width="6" height="11" viewBox="0 0 6 11"><path d="M0 4 3 1l3 3zM0 7l3 3 3-3z" fill="#444"/></svg></div></div>
      <div class="add-btn"><svg width="7" height="7" viewBox="0 0 7 7"><path d="M0 2h7L6 6H1z" fill="#fff"/></svg>ADD TO CART</div>
    </div>
  </div>
  <div class="abs product" style="left:279px;top:563px">
    <div class="product-photo" role="img" aria-label="Photo of a 5 gallon black pail of lubricant"></div>
    <div class="product-base">
      <div class="qty"><span class="qty-label">QTY:</span><div class="qty-box">1<svg width="6" height="11" viewBox="0 0 6 11"><path d="M0 4 3 1l3 3zM0 7l3 3 3-3z" fill="#444"/></svg></div></div>
      <div class="add-btn"><svg width="7" height="7" viewBox="0 0 7 7"><path d="M0 2h7L6 6H1z" fill="#fff"/></svg>ADD TO CART</div>
    </div>
  </div>
  <div class="abs product" style="left:449px;top:563px">
    <div class="product-photo" role="img" aria-label="Photo of a 5 gallon black pail of lubricant"></div>
    <div class="product-base">
      <div class="qty"><span class="qty-label">QTY:</span><div class="qty-box">0<svg width="6" height="11" viewBox="0 0 6 11"><path d="M0 4 3 1l3 3zM0 7l3 3 3-3z" fill="#444"/></svg></div></div>
      <div class="add-btn"><svg width="7" height="7" viewBox="0 0 7 7"><path d="M0 2h7L6 6H1z" fill="#fff"/></svg>ADD TO CART</div>
    </div>
  </div>

  <div class="abs cart">
    <div class="cart-title">My cart</div>
    <div class="cart-line"></div>
    <div class="cart-total">$ 130.00</div>
    <div class="cart-qty">for 5 gallons</div>
    <div class="cart-action" style="top:0">
      <svg width="26" height="22" viewBox="0 0 26 22"><path d="M1 2h4l3 12h13l3-9H7" fill="none" stroke="#fff" stroke-width="2.4" stroke-linejoin="round"/><circle cx="10" cy="19" r="2" fill="#fff"/><circle cx="19" cy="19" r="2" fill="#fff"/></svg>
      view cart
    </div>
    <div class="cart-action" style="top:66px;height:64px">
      <svg width="24" height="22" viewBox="0 0 24 22"><path d="M2 10 11 1h9v9l-9 9z" fill="#fff"/><circle cx="16" cy="5" r="1.6" fill="#4b6d92"/><text x="10" y="14" font-size="8" font-weight="700" fill="#4b6d92" font-family="Open Sans,sans-serif">$</text></svg>
      checkout
    </div>
  </div>
</main>

<section class="abs checkout">
  <div class="fine" style="left:352px;top:3px">Your order is safe &amp; secure, all transactions are encrypted.</div>
  <div class="pay-card">
    <div class="tabs"><span>Pay by Credit Card</span><span>Pay via PouchPay</span></div>
    <div class="summary">
      <div>YOUR ORDER</div>
      <div class="summary-item">5 Gallons of knuckle balm</div>
      <div class="summary-price"><span style="font-size:4px;display:block;text-align:right">TOTAL COST</span>$130.00</div>
      <div class="lbl" style="left:6px;top:42px">First name</div>
      <div class="fld" style="left:6px;top:47px;width:44px">Harriet</div>
      <div class="lbl" style="left:57px;top:42px">Last name</div>
      <div class="fld" style="left:57px;top:47px;width:44px">Vale</div>
      <div class="lbl" style="left:6px;top:60px">Email address</div>
      <div class="fld" style="left:6px;top:65px;width:95px">hvale@example.net</div>
    </div>
    <div class="lbl" style="left:140px;top:26px">Name as written on card</div>
    <div class="fld" style="left:140px;top:31px;width:124px">Ms H Vale</div>
    <div class="lbl" style="left:140px;top:45px">Billing street address</div>
    <div class="fld" style="left:140px;top:50px;width:80px">22 a Marlow Terrace</div>
    <div class="lbl" style="left:224px;top:45px">Postcode</div>
    <div class="fld" style="left:224px;top:50px;width:40px">NE4 7QT</div>
    <div class="lbl" style="left:140px;top:64px">Credit card number</div>
    <div class="fld" style="left:140px;top:69px;width:124px">1234 5678 9101 1121</div>
    <div class="lbl" style="left:140px;top:83px">Expiry date</div>
    <div class="fld" style="left:140px;top:88px;width:47px">January</div>
    <div class="fld" style="left:191px;top:88px;width:30px">2012</div>
    <div class="lbl" style="left:224px;top:83px">CVV</div>
    <div class="fld" style="left:224px;top:88px;width:40px">999</div>
    <div class="order-btn">Place your order</div>
  </div>
  <div class="fine" style="left:324px;top:143px">We do not store your card information.</div>
  <div class="fine" style="left:404px;top:143px">Powered by Ledgerly</div>
</section>

<footer class="abs footer">
  <h3 style="left:121px">More About Company</h3>
  <p class="about-copy">Lorem ipsum dolor sit amet, consectetur adipiscing elit. Duis dapibus rhoncus purus, quis aliquet urna vehicula eu. Maecenas velit orci, volutpat sed posuere eu, vehicula eu tellus. Pellentesque sem sapien, aliquet id rhoncus eget, interdum vitae ligula.</p>
  <p class="signoff">- Oliver Penrose, <b>CEO</b></p>

  <h3 style="left:337px">Keep Connected</h3>
  <ul class="follow">
    <li><span></span>Like us on Friendwall</li>
    <li><span></span>Follow us on Chirper</li>
    <li class="hl"><span></span>Add us on Circlesphere</li>
    <li><span></span>Follow us on Workline</li>
    <li><span></span>Subscribe to our RSS</li>
  </ul>

  <h3 style="left:494px">Contact Information</h3>
  <div class="contact">
    <div class="row">
      <svg width="8" height="8" viewBox="0 0 8 8"><path d="M4 0 0 4h1v4h2V5h2v3h2V4h1z" fill="#ddd"/></svg>
      <div>Ada Fenwick<br><br>38 Linden Row<br><br>Hartfield, HF2 8LR</div>
    </div>
    <div class="row">
      <svg width="8" height="8" viewBox="0 0 8 8"><rect x="2" y="0" width="4" height="8" rx="1" fill="#ddd"/></svg>
      <div style="color:#fff">0845 000 4419</div>
    </div>
    <div class="row">
      <svg width="8" height="8" viewBox="0 0 8 8"><path d="M0 2h8v5H0z" fill="#ddd"/><path d="M0 2l4 3 4-3" fill="none" stroke="#2b2b2b" stroke-width=".8"/></svg>
      <a href="#">hello@knucklebalm.test</a>
    </div>
  </div>
</footer>

</body>
</html>
```